Webpage needed for a new legal recruitment/headhunting companyi

I would like a professional and sharp looking website to showcase a new legal headhunting/recruitment company called Mosswick. The logo for the company is attached.

I like the following websites:
http://www.brindletalent.co.uk/
(For the general style and layout- although photographs of the team will be difficult as we don't have one yet!;-))

http://qorv.co.uk/
I like the style of the photographs etc on this one.

NB the pictures attached below are for information only- I don't think I would be able to use any of them...

Hope you can help!
Many thanks

Industry/Entity Type

Legal

```html
<!DOCTYPE html>
<html lang="en">
<head>
<meta charset="utf-8">
<title>Mosswick Legal Recruitment</title>
<link href="https://fonts.googleapis.com/css2?family=Open+Sans:wght@300;400;600&display=swap" rel="stylesheet">
<style>
:root{
  --purple:#4b2f6b;
  --purple-mid:#5e3d84;
  --purple-light:#7a5aa0;
  --ink:#555;
  --ink-soft:#6a6a6a;
  --grey-bg:#ececec;
  --rule:#d2d2d2;
  --white:#fff;
}
*{margin:0;padding:0;box-sizing:border-box}
html,body{width:1199px;height:1200px;overflow:hidden}
body{position:relative;font-family:"Open Sans",Arial,sans-serif;color:var(--ink);background:var(--grey-bg)}
.abs{position:absolute}
.header-band{left:0;top:0;width:1199px;height:128px;background:var(--white)}
.footer-band{left:0;top:1043px;width:1199px;height:157px;background:var(--purple)}
.content-panel{left:120px;top:400px;width:960px;height:668px;background:var(--white)}

.brand{left:131px;top:22px;display:flex;align-items:center;gap:8px}
.brand-name{font-size:44px;font-weight:300;color:var(--purple);letter-spacing:1px;line-height:1}
.brand-tag{left:236px;top:68px;font-size:11px;color:#888}

.main-nav{right:129px;top:59px;display:flex;gap:18px;font-size:14px;text-transform:uppercase;color:#444;letter-spacing:.3px}
.main-nav .sep{color:#444}
.main-nav .active{color:var(--purple);font-weight:600}

.hero{left:129px;top:103px;width:942px;height:333px;border:3px solid var(--white);box-shadow:0 0 0 1px #ddd,0 10px 14px -8px rgba(0,0,0,.35);background:linear-gradient(100deg,#b9c4cf 0%,#cfd8e0 35%,#8d949c 55%,#3b3e44 75%,#c9d3dc 100%)}
.hero-caption{left:3px;height:53px;background:rgba(40,40,40,.72);color:var(--white);font-size:30px;font-weight:600;letter-spacing:.5px;padding:6px 22px;line-height:40px;white-space:nowrap}
.hero-dots{left:22px;top:295px;display:flex;gap:6px}
.hero-dots span{width:15px;height:15px;border-radius:50%;background:#333}
.hero-dots span.on{background:var(--purple)}

.welcome-title{left:142px;top:482px;font-size:27px;font-weight:300;color:#8a8a8a;display:flex;align-items:center;gap:8px}
.welcome-title b{font-weight:400;font-size:19px;color:var(--purple);display:flex;align-items:center;gap:4px}
.welcome-text{left:142px;top:524px;width:470px;font-size:13.4px;line-height:23px;color:var(--ink)}

.tile{width:180px;height:96px;border:1px solid #cfcfcf;background:linear-gradient(#f4f4f4,#d8d8d8);display:flex;align-items:center;gap:14px;padding-left:14px;font-size:15px;line-height:22px;color:#444;letter-spacing:.3px}
.tile.featured{background:linear-gradient(#6c4b92,#4d2f6f);color:var(--white);border-color:#4d2f6f}

.rule{left:130px;width:940px;height:1px;background:var(--rule)}
.seen-title{left:0;width:1199px;top:742px;text-align:center;font-size:26px;color:#8a8a8a}
.seen-title span{color:var(--purple)}
.press-row{left:150px;top:800px;width:900px;display:flex;justify-content:space-between;align-items:center;font-size:17px;color:#444;letter-spacing:.3px}

.story-img{width:192px;height:126px;border:1px solid #ccc}
.story-title{font-size:16px;line-height:20px;color:var(--purple);width:215px}
.story-text{font-size:12.4px;line-height:20px;color:var(--ink-soft);width:230px}
.story-link{font-size:12px;color:var(--purple);letter-spacing:.5px}

.footer-nav{left:129px;top:1098px;font-size:14px;color:var(--white);display:flex;gap:8px}
.copyright{left:130px;top:1144px;font-size:12.5px;color:#a995c0}
.social{left:931px;top:1102px;display:flex;gap:7px}
.social span{width:30px;height:30px;border-radius:4px;background:var(--purple-light)}
</style>
</head>
<body>
<div class="abs header-band"></div>
<div class="abs footer-band"></div>
<div class="abs content-panel"></div>

<header>
  <div class="abs brand">
    <span class="brand-name">Mosswick</span>
    <svg width="16" height="16" viewBox="0 0 16 16"><circle cx="8" cy="8" r="7" fill="var(--purple)"/></svg>
  </div>
  <div class="abs brand-tag">Legal Recruitment</div>
  <nav class="abs main-nav">
    <span class="active">Home</span><span class="sep">/</span>
    <span>Candidates</span><span class="sep">/</span>
    <span>Our Team</span><span class="sep">/</span>
    <span>Clients</span><span class="sep">/</span>
    <span>Advice</span><span class="sep">/</span>
    <span>Contact</span>
  </nav>
</header>

<section class="abs hero" role="img" aria-label="Three lawyers in suits standing before city office towers">
  <div class="abs hero-caption" style="top:104px;width:470px">We are in Legal Headhunting</div>
  <div class="abs hero-caption" style="top:161px;width:431px">and Recruitment Company</div>
  <div class="abs hero-dots"><span class="on"></span><span></span><span></span><span></span></div>
</section>

<section>
  <h1 class="abs welcome-title">Welcome to <b><svg width="10" height="10"><circle cx="5" cy="5" r="5" fill="var(--purple)"/></svg>Mosswick</b></h1>
  <p class="abs welcome-text">Aliquam molestie, mi et imperdiet euismod, dui purus auctor tellus, et interdum lacus lectus et ante. Sed accumsan sollicitudin sapien, sit amet adipiscing turpis gravida ac. In congue, neque ac lobortis volutpat, libero mauris varius mi, vitae suscipit ipsum ligula vitae risus. Duis aliquam nibh a dui iaculis viverra id a velit. Vivamus egestas risus in magna varius commodo. Sed semper viverra egestas. Etiam pretium porttitor lectus, vel ornare neque porta volutpat.</p>

  <div class="abs tile featured" style="left:689px;top:490px">
    <svg width="42" height="28" viewBox="0 0 42 28" fill="#fff"><circle cx="21" cy="7" r="5"/><path d="M12 26c0-7 4-11 9-11s9 4 9 11z"/><circle cx="9" cy="9" r="4"/><path d="M1 26c0-6 3-9 8-9 2 0 3 .5 4 1-1 2-2 5-2 8z"/><circle cx="33" cy="9" r="4"/><path d="M41 26c0-6-3-9-8-9-2 0-3 .5-4 1 1 2 2 5 2 8z"/></svg>
    <span>What We Are<br>Working On</span>
  </div>
  <div class="abs tile" style="left:878px;top:490px">
    <svg width="40" height="34" viewBox="0 0 40 34" fill="var(--purple)"><path d="M10 2h20v10c0 6-4 10-10 10S10 18 10 12z"/><path d="M10 5H3c0 6 3 10 8 10v-3c-3 0-5-2-5-4h4zM30 5h7c0 6-3 10-8 10v-3c3 0 5-2 5-4h-4z"/><rect x="17" y="21" width="6" height="6"/><rect x="12" y="27" width="16" height="5"/></svg>
    <span>Recent<br>Successes</span>
  </div>
  <div class="abs tile" style="left:689px;top:595px">
    <svg width="42" height="28" viewBox="0 0 42 28"><rect x="2" y="4" width="38" height="20" rx="2" fill="var(--purple)" transform="rotate(-8 21 14)"/><circle cx="21" cy="14" r="5" fill="#ddd"/></svg>
    <span>Real Salaries</span>
  </div>
  <div class="abs tile" style="left:878px;top:595px">
    <svg width="40" height="36" viewBox="0 0 40 36" fill="var(--purple)"><ellipse cx="21" cy="15" rx="18" ry="14"/><path d="M6 24 2 34l12-6z"/></svg>
    <span>Client's<br>Testimonials</span>
  </div>
</section>

<div class="abs rule" style="top:726px"></div>
<h2 class="abs seen-title" style="font-weight:400">As Seen <span>on</span></h2>
<div class="abs press-row">
  <span>Harbor Business Review</span>
  <span>Ledgerline</span>
  <span>Metro Nine</span>
  <span>Market Courier</span>
  <span>Circuit Daily</span>
  <span>Coastal Herald</span>
</div>
<div class="abs rule" style="top:862px"></div>

<article>
  <div class="abs story-img" role="img" aria-label="Harbour town on green hills beside a turquoise bay" style="left:143px;top:892px;background:linear-gradient(#cfe0ee 0%,#6f8a5a 40%,#3ea3b0 62%,#c8b8a4 100%)"></div>
  <h3 class="abs story-title" style="left:353px;top:888px;font-weight:400">Nam fermentum vestibulum purus id</h3>
  <p class="abs story-text" style="left:353px;top:932px">Vivamus egestas risus in magna varius commodo. Sed semper viverraegestas. Etiam pretium porttitor lectus, vel ornare neque porta volutpat.</p>
  <span class="abs story-link" style="left:353px;top:1030px">LEARN MORE &gt;&gt;</span>
</article>
<article>
  <div class="abs story-img" role="img" aria-label="Dictionary, glasses and pen resting on a printed CV" style="left:622px;top:892px;background:linear-gradient(135deg,#2a2a2a 0%,#6b6b6b 45%,#b9b9b9 100%)"></div>
  <h3 class="abs story-title" style="left:832px;top:888px;font-weight:400">Nam fermentum vestibulum purus id</h3>
  <p class="abs story-text" style="left:832px;top:932px">Vivamus egestas risus in magna varius commodo. Sed semper viverraegestas. Etiam pretium porttitor lectus, vel ornare neque porta volutpat.</p>
  <span class="abs story-link" style="left:832px;top:1030px">LEARN MORE &gt;&gt;</span>
</article>

<footer>
  <nav class="abs footer-nav">
    <span>Home</span><span>/</span><span>Candidates</span><span>/</span><span>Our Team</span><span>/</span><span>Clients</span><span>/</span><span>Advice</span><span>/</span><span>Contact</span>
  </nav>
  <p class="abs copyright">Copyright © 2014. Mosswick. All Right Reserved</p>
  <div class="abs social" aria-label="Social links"><span></span><span></span><span></span><span></span></div>
</footer>
</body>
</html>
```